Business Card Design

I'm a young beekeeper (22 years old) just starting out. I own and run 80 hives and would like to eventually build up to 1000. My aim is to run it in tandem with our family farm that is currently running sheep and beef. Unlike a number of honey companies on the East Coast (or the North Island, NZ) I am local and will expand onto the lease blocks that our family is also leasing. I want a simple plain logo/photo. The designer may wish to use one of the photos as a background outline or however they chose. The mountain is Moekaha and our farm borders one side of it.

Target Market(s)

From local land owners to wholesale honey buyers

Industry/Entity Type

Farm

Contact Information for Business Card

Moekaha Honey
Manager Owner Rewene Tolland
email moekahahoney@pelvanmail.co.nz
mobile 0219473061

Requirements
Must have
• The details submitted. The brand Moekaha Honey to be the main feature. The other details can be smaller.
Should not have
• Must not include a picture of a bee or hive. Use a modern font. Don't use koru but may incorporate poutama.

```html
<!DOCTYPE html>
<html lang="en">
<head>
<meta charset="utf-8">
<title>Moekaha Honey – Business Card</title>
<link rel="stylesheet" href="https://fonts.googleapis.com/css2?family=Roboto:wght@300;400;700&display=swap">
<style>
  :root {
    --backdrop: #3a2a33;
    --navy: #1e2d4d;
    --navy-soft: #34456a;
    --amber: #e58d1c;
    --yellow: #f8df22;
    --gold: #f2c41a;
    --sky: #eef2f5;
    --mist: #b9c6d2;
    --mountain: #4d6783;
    --paper: #ffffff;
  }
  * { box-sizing: border-box; margin: 0; padding: 0; }
  html, body {
    width: 1200px;
    height: 865px;
    overflow: hidden;
    background: var(--backdrop);
  }
  .card {
    position: absolute;
    left: 150px;
    top: 175px;
    width: 900px;
    height: 514px;
    background: var(--paper);
    overflow: hidden;
    box-shadow: 0 18px 40px rgba(0,0,0,.35);
  }
  .card__landscape {
    position: absolute;
    inset: 0 0 194px 0;
    background: linear-gradient(180deg, var(--sky) 0%, var(--sky) 18%, var(--mist) 45%, var(--mountain) 80%, #5f7689 100%);
  }
  .brand {
    position: absolute;
    left: 0; right: 0;
    top: 118px;
    text-align: center;
    font-family: "Roboto", sans-serif;
    font-weight: 700;
    font-size: 62px;
    letter-spacing: 4px;
    color: var(--navy);
  }
  .band {
    position: absolute;
    left: 0; right: 0; bottom: 0;
    height: 194px;
    background: linear-gradient(90deg, var(--amber) 0%, var(--yellow) 50%, var(--gold) 75%, var(--amber) 100%);
    border-top: 3px solid var(--navy-soft);
  }
  .person {
    position: absolute;
    left: 70px;
    bottom: 44px;
    font-family: "Roboto", sans-serif;
    color: var(--navy);
  }
  .person__name {
    font-weight: 700;
    font-size: 30px;
    letter-spacing: .5px;
  }
  .person__role {
    font-weight: 300;
    font-size: 18px;
    letter-spacing: 1px;
    margin-top: 2px;
  }
  .band__divider {
    position: absolute;
    left: 560px;
    top: 22px;
    width: 1px;
    height: 110px;
    background: var(--navy-soft);
    opacity: .6;
  }
  .contact {
    position: absolute;
    left: 585px;
    top: 30px;
    list-style: none;
    font-family: "Roboto", sans-serif;
    font-size: 17px;
    color: var(--navy);
  }
  .contact__item {
    display: flex;
    align-items: center;
    gap: 12px;
    height: 34px;
  }
  .contact__icon { width: 16px; height: 16px; flex: none; }
</style>
</head>
<body>
  <article class="card">
    <div class="card__landscape" role="img" aria-label="Photograph of Moekaha mountain rising above a lake under a pale sky"></div>

    <h1 class="brand">MOEKAHA HONEY</h1>

    <section class="band">
      <div class="person">
        <p class="person__name">REWENE TOLLAND</p>
        <p class="person__role">MANAGER OWNER</p>
      </div>

      <span class="band__divider"></span>

      <ul class="contact">
        <li class="contact__item">
          <svg class="contact__icon" viewBox="0 0 16 16" aria-hidden="true">
            <path fill="#1e2d4d" d="M3.2 1.5l2.3 2.6-1.3 1.8c.9 2 2.4 3.5 4.3 4.4l1.8-1.3 2.6 2.3-1.4 2.2C6.4 13.3 2.7 9.6 1 4.6z"/>
          </svg>
          <span>021 947 3061</span>
        </li>
        <li class="contact__item">
          <svg class="contact__icon" viewBox="0 0 16 16" aria-hidden="true">
            <rect x="1" y="3" width="14" height="10" fill="#1e2d4d"/>
            <path d="M1.5 3.5L8 9l6.5-5.5" fill="none" stroke="#f2c41a" stroke-width="1.2"/>
          </svg>
          <span>moekahahoney@pelvanmail.co.nz</span>
        </li>
      </ul>
    </section>
  </article>
</body>
</html>
```